Postcard Design

Landscaping Company
Lawn Cuts
Mulch
Spring Clean Ups
Planting

Company Name - RVM GROUNDWORK PARTNERS
ADDRESS - 47 Kestwick Rd.
N. Hanover, NJ 08599
Phone #- 609-555-0148

Target Market(s)

Direct mailer looking to draw in new clients

Industry/Entity Type

It Company

Requirements
Must have
• Eye catching

```html
<!DOCTYPE html>
<html lang="en">
<head>
<meta charset="utf-8">
<title>RVM Groundwork Partners – Spring Postcard</title>
<link rel="stylesheet" href="https://fonts.googleapis.com/css2?family=Crimson+Text:wght@400;600;700&display=swap">
<style>
  :root {
    --brown: #7a4320;
    --brown-dark: #5e3116;
    --frame: #f2f0e8;
    --sky-top: #4fa3e0;
    --sky-mid: #bcdcf3;
    --tree: #3f6b33;
    --grass-light: #7fc04a;
    --grass-dark: #3f8a22;
    --white: #ffffff;
    --rule: #b9b9b9;
  }
  * { box-sizing: border-box; margin: 0; padding: 0; }
  html, body { width: 773px; height: 1200px; overflow: hidden; background: var(--white); }
  body { font-family: "Crimson Text", Georgia, serif; position: relative; }

  .front {
    position: absolute; left: 0; top: 0; width: 773px; height: 598px; overflow: hidden;
  }
  .front-scene {
    position: absolute; inset: 0;
    background: linear-gradient(180deg, var(--sky-top) 0%, var(--sky-mid) 26%, #e6f2fa 34%, var(--tree) 38%, #55863a 43%, var(--grass-light) 50%, var(--grass-dark) 100%);
  }
  .headline {
    position: absolute; left: 22px; top: 10px; color: var(--brown);
    font-weight: 700; line-height: 1;
  }
  .headline .big { font-size: 44px; }
  .headline .small { font-size: 20px; font-weight: 600; }
  .headline .line2 { display: block; margin-left: 176px; margin-top: -4px; }
  .offer {
    position: absolute; left: 259px; top: 114px; font-size: 17px; font-weight: 700; color: var(--brown);
  }

  .snapshot {
    position: absolute; background: var(--frame); padding: 10px 10px 0;
    box-shadow: 2px 4px 10px rgba(0,0,0,.35);
  }
  .snapshot .photo { width: 100%; }
  .snapshot .label {
    text-align: center; color: var(--brown); font-weight: 700; font-size: 30px; line-height: 1; padding: 8px 0 10px;
    white-space: nowrap;
  }
  .snap-cleaning { z-index: 1; left: 156px; top: 282px; width: 240px; transform: rotate(4deg); }
  .snap-cleaning .photo { height: 222px; background: linear-gradient(150deg, #c9682a, #e89a3e 50%, #8a3e17); }
  .snap-planting { z-index: 2; left: 360px; top: 202px; width: 252px; transform: rotate(-3deg); }
  .snap-planting .photo { height: 232px; background: linear-gradient(170deg, #77a84d, #d3405f 45%, #e8b33a 70%, #8c7f63); }
  .snap-landscaping { z-index: 3; left: -14px; top: 184px; width: 222px; transform: rotate(-5deg); }
  .snap-landscaping .photo { height: 218px; background: linear-gradient(160deg, #9cc7e8, #6f8f5a 55%, #3c7a2a); }
  .snap-landscaping .label { font-size: 28px; padding-left: 8px; }
  .snap-mowing { z-index: 2; left: 592px; top: -24px; width: 210px; transform: rotate(10deg); }
  .snap-mowing .photo { height: 214px; background: linear-gradient(180deg, #5c8a3e, #6fb23b 40%, #3f8a22); }
  .snap-mulch { z-index: 3; left: 606px; top: 266px; width: 200px; transform: rotate(10deg); }
  .snap-mulch .photo { height: 236px; background: linear-gradient(170deg, #a9a59c, #6b4a2e 55%, #4a2f1c); }

  .back-panel {
    position: absolute; left: 0; top: 602px; width: 316px; height: 598px; overflow: hidden; color: var(--white);
  }
  .back-scene {
    position: absolute; inset: 0;
    background: linear-gradient(180deg, var(--sky-top) 0%, #a7d1ef 30%, #e3f0f8 40%, #e9f2f6 46%, var(--tree) 49%, #5a8d3a 56%, var(--grass-light) 62%, var(--grass-dark) 100%);
  }
  .company { position: absolute; left: 27px; top: 22px; color: var(--brown-dark); font-size: 19px; line-height: 1.2; font-style: normal; }
  .company-name { font-weight: 400; letter-spacing: .3px; }
  .cta { position: absolute; left: 46px; top: 424px; font-size: 19px; font-weight: 700; line-height: 1.15; }
  .phone { position: absolute; left: 46px; top: 484px; font-size: 36px; font-weight: 700; }

  .address-lines { position: absolute; left: 364px; top: 980px; width: 376px; }
  .address-lines span { display: block; height: 0; border-top: 1px solid var(--rule); margin-bottom: 50px; }
</style>
</head>
<body>
  <section class="front">
    <div class="front-scene" role="img" aria-label="Sunny sky over a row of trees and a wide green lawn"></div>
    <h1 class="headline">
      <span class="big">Spring</span> <span class="small">is around the corner</span>
      <span class="line2"><span class="small">and we are here to</span> <span class="big">help.</span></span>
    </h1>
    <p class="offer">We offer complete services from:</p>

    <figure class="snapshot snap-cleaning">
      <div class="photo" role="img" aria-label="Rake gathering autumn leaves"></div>
      <figcaption class="label">Spring Cleaning</figcaption>
    </figure>
    <figure class="snapshot snap-planting">
      <div class="photo" role="img" aria-label="Flower bed with colourful blooms and boulders"></div>
      <figcaption class="label">Planting</figcaption>
    </figure>
    <figure class="snapshot snap-landscaping">
      <div class="photo" role="img" aria-label="Landscaped backyard with a pool, house and garden beds"></div>
      <figcaption class="label">Landscaping</figcaption>
    </figure>
    <figure class="snapshot snap-mowing">
      <div class="photo" role="img" aria-label="Freshly mowed lawn with striped grass"></div>
      <figcaption class="label">Mowing</figcaption>
    </figure>
    <figure class="snapshot snap-mulch">
      <div class="photo" role="img" aria-label="Mulched garden bed beside a brick house"></div>
      <figcaption class="label">Mulch</figcaption>
    </figure>
  </section>

  <section class="back-panel">
    <div class="back-scene" role="img" aria-label="Blue sky with clouds above a tree line and green field"></div>
    <address class="company">
      <div class="company-name">RVM GROUNDWORK PARTNERS</div>
      <div>47 Kestwick Rd.</div>
      <div>N. Hanover, NJ 08599</div>
    </address>
    <p class="cta">Call us today for the<br>best price in town!</p>
    <p class="phone">609-555-0148</p>
  </section>

  <div class="address-lines" aria-hidden="true"><span></span><span></span><span></span></div>
</body>
</html>
```